" Clinica de radiologia especializada em diagnóstico para odontologia. Compromisso com a qualidade e tecnologia de seus equipamentos. Mais de 50 mil pacientes atendidos. "

```html
<!DOCTYPE html>
<html lang="pt-BR">
<head>
<meta charset="utf-8">
<title>Cartão de visitas – Clara Visão Radiologia</title>
<link href="https://fonts.googleapis.com/css2?family=Open+Sans:wght@400;600;700&display=swap" rel="stylesheet">
<style>
  :root{
    --page:#ececec;
    --card-top:#fdfdfd;
    --card-bottom:#ededed;
    --name-gray:#6f6f6f;
    --green:#1f6b4c;
    --back-top:#9a9a9a;
    --back-bottom:#6e6e6e;
    --text-light:#ffffff;
    --text-soft:#e4e4e4;
    --shadow:rgba(0,0,0,.28);
  }
  *{margin:0;padding:0;box-sizing:border-box}
  html,body{width:1200px;height:1200px;overflow:hidden;background:var(--page)}
  body{font-family:"Open Sans",Arial,sans-serif;position:relative}

  .card{
    position:absolute;left:340px;width:520px;height:290px;
    border-radius:22px;overflow:hidden;
    box-shadow:4px 6px 0 var(--shadow);
  }
  .card--front{
    top:250px;
    background:linear-gradient(180deg,var(--card-top),var(--card-bottom));
  }
  .brand-name{
    position:absolute;left:0;right:0;top:118px;text-align:center;
    font-size:30px;font-weight:600;color:var(--name-gray);letter-spacing:.5px;
  }
  .website{
    position:absolute;left:0;right:0;bottom:22px;text-align:center;
    font-size:12px;font-weight:700;color:var(--green);letter-spacing:.3px;
  }

  .card--back{
    top:600px;
    background:linear-gradient(160deg,var(--back-top),var(--back-bottom));
    color:var(--text-light);
  }
  .back-panel{
    position:absolute;right:0;top:0;width:180px;height:290px;
    background:linear-gradient(90deg,rgba(255,255,255,0),rgba(255,255,255,.22));
  }
  .back-info{position:absolute;left:30px;top:28px;width:300px}
  .back-info__company{font-size:17px;font-weight:700;letter-spacing:.3px}
  .back-info__sub{font-size:10px;font-weight:600;color:var(--text-soft);margin-top:2px}
  .back-info__rule{height:1px;background:var(--text-soft);margin:18px 0 10px;width:300px}
  .back-info__person{font-size:12px;font-weight:700;letter-spacing:.5px}
  .back-info__role{font-size:8px;color:var(--text-soft);margin-top:2px}
  .contact{font-size:12px;margin-top:16px;line-height:1.5}
  .contact__prefix{font-size:8px;vertical-align:middle;margin-right:3px}
  .contact--address{margin-top:12px}
</style>
</head>
<body>
  <section class="card card--front" aria-label="Frente do cartão">
    <p class="brand-name">Clara Visão Radiologia</p>
    <p class="website">claravisaoradiologia.com.br</p>
  </section>

  <section class="card card--back" aria-label="Verso do cartão">
    <div class="back-panel" role="img" aria-label="Área decorativa em tons de cinza claro"></div>
    <div class="back-info">
      <h1 class="back-info__company">CLARA VISÃO RADIOLOGIA</h1>
      <p class="back-info__sub">Clínica de Radiologia e Documentação Odontológica</p>
      <div class="back-info__rule"></div>
      <p class="back-info__person">MARINA S. DORVAL PRATES</p>
      <p class="back-info__role">Responsável Técnica CRO 0000</p>
      <p class="contact"><span class="contact__prefix">(47)</span>3210-4455</p>
      <p class="contact">claravisao.adm@exemplo.com</p>
      <p class="contact contact--address">R: Padre Anselmo Dias,<br>212 - B: Centro - Navegantes - SC</p>
    </div>
  </section>
</body>
</html>
```